Author/ Speaker Business Card design

I need a business card designed that will go with the branding that is already on my book and website. I like clean and straightforward, but I am not opposed to something more 'innovative'.

Target Market(s)

Colleges and Universities, educational institutions

Industry/Entity Type

Education

Contact Information for Business Card

Standard size. It should be able to be printed on good quality white or ivory paper.

Font styles to use
Sans Serif

Colors
0355a3

Requirements
Must have
• There's a blue on my website. It should have some blue. My logo is at the top. It should have the logo incorporated somewhere on it. My name, Author | Speaker | Teacher | Trainer, my phone number (+31 64-207 5819), my email address (milo@theboldlearner.example), Social media icons (twitter, Instagram, LinkedIn) with the addresses (twitter @writermilofenwick, Instagram - theboldlearner, LinkedIn - theboldlearner) By they way, the website is www.theboldlearner.example. There is a photo of the book on the website. Also, my full name is Milo Fenwick
Nice to have
• Try to use the font that is on the website and book. Also, if you could get that blue, that would be great.
Should not have
• My photo

```html
<!DOCTYPE html>
<html lang="en">
<head>
<meta charset="utf-8">
<title>The Bold Learner – Business Card</title>
<link rel="stylesheet" href="https://fonts.googleapis.com/css2?family=Questrial&family=Open+Sans:wght@400;600&display=swap">
<style>
  :root {
    --brand-blue: #2b4c9b;
    --brand-blue-deep: #1c3478;
    --brand-blue-light: #4467b4;
    --ink-grey: #555b66;
    --paper: #ffffff;
    --backdrop: #e6e7ea;
  }
  * { box-sizing: border-box; margin: 0; padding: 0; }
  html, body { width: 1200px; height: 1200px; overflow: hidden; }
  body {
    background: var(--backdrop);
    display: flex;
    align-items: center;
    justify-content: center;
    gap: 100px;
    font-family: "Open Sans", sans-serif;
  }
  .card {
    position: relative;
    width: 380px;
    height: 664px;
    overflow: hidden;
    box-shadow: 0 10px 30px rgba(0,0,0,0.18);
  }

  /* Title set in the card's text font, one size and weight */
  .card-title {
    font-family: "Open Sans", sans-serif;
    font-weight: 600;
    font-size: 58px;
    line-height: 1.08;
    letter-spacing: 0;
  }
  .card-title span { display: block; }

  /* Front side */
  .card--front { background: var(--paper); }
  .card--front .card-title { position: absolute; top: 70px; left: 44px; color: var(--brand-blue); }

  .contact-list {
    position: absolute;
    top: 318px;
    left: 52px;
    list-style: none;
    font-size: 15px;
    color: var(--ink-grey);
  }
  .contact-list li { display: flex; align-items: center; gap: 9px; height: 26px; }
  .contact-list .gap { margin-top: 14px; }
  .contact-icon { width: 15px; height: 15px; flex: none; }
  .contact-icon--plain { background: var(--brand-blue-light); border-radius: 2px; }

  .brand-line {
    position: absolute;
    right: 32px;
    bottom: 130px;
    display: flex;
    align-items: center;
    gap: 12px;
    color: var(--brand-blue);
    font-size: 26px;
    font-weight: 600;
  }
  .brand-line__mark { width: 36px; height: 36px; background: var(--brand-blue); }

  .name-band {
    position: absolute;
    left: 0; right: 0; bottom: 0;
    height: 104px;
    background: linear-gradient(180deg, var(--brand-blue-light), var(--brand-blue));
    color: var(--paper);
    text-align: center;
    padding-top: 24px;
  }
  .name-band__name { font-family: "Questrial", sans-serif; font-size: 32px; letter-spacing: 7px; text-transform: uppercase; }
  .name-band__roles { font-size: 11px; margin-top: 6px; letter-spacing: 0.3px; }

  /* Back side */
  .card--back {
    background: radial-gradient(circle at 45% 38%, var(--brand-blue-light) 0%, var(--brand-blue) 45%, var(--brand-blue-deep) 100%);
    color: var(--paper);
  }
  .card--back .card-title { position: absolute; top: 170px; left: 0; right: 0; text-align: center; }
  .tagline {
    position: absolute;
    top: 440px;
    left: 0; right: 0;
    text-align: center;
    font-size: 17px;
    line-height: 1.75;
    letter-spacing: 2px;
    text-transform: uppercase;
  }
</style>
</head>
<body>

  <section class="card card--front" aria-label="Card front">
    <h1 class="card-title">
      <span>The Bold</span>
      <span>Learner</span>
    </h1>

    <ul class="contact-list">
      <li><span class="contact-icon contact-icon--plain"></span>@writermilofenwick</li>
      <li><span class="contact-icon contact-icon--plain"></span>theboldlearner</li>
      <li class="gap">
        <svg class="contact-icon" viewBox="0 0 16 16"><rect width="16" height="16" rx="3" fill="#4467b4"/><path d="M5 3.5l2 2-1 1.3c.6 1.3 1.6 2.3 2.9 2.9l1.3-1 2 2-1.3 1.6C7.5 12 4 8.5 3.6 4.6z" fill="#fff"/></svg>
        +31 64-207 5819
      </li>
      <li>
        <svg class="contact-icon" viewBox="0 0 16 16"><rect width="16" height="16" rx="3" fill="#4467b4"/><rect x="3" y="4.5" width="10" height="7" fill="none" stroke="#fff" stroke-width="1.2"/><path d="M3 4.5l5 4 5-4" fill="none" stroke="#fff" stroke-width="1.2"/></svg>
        milo@theboldlearner.example
      </li>
      <li>
        <svg class="contact-icon" viewBox="0 0 16 16"><rect width="16" height="16" rx="3" fill="#4467b4"/><circle cx="8" cy="8" r="4.6" fill="none" stroke="#fff" stroke-width="1.1"/><path d="M3.4 8h9.2M8 3.4c-2.4 2.6-2.4 6.6 0 9.2M8 3.4c2.4 2.6 2.4 6.6 0 9.2" fill="none" stroke="#fff" stroke-width="1"/></svg>
        www.theboldlearner.example
      </li>
    </ul>

    <div class="brand-line">
      <span class="brand-line__mark"></span>
      <span class="brand-line__name">The Bold Learner</span>
    </div>

    <div class="name-band">
      <p class="name-band__name">Milo Fenwick</p>
      <p class="name-band__roles">Author | Speaker | Teacher | Trainer</p>
    </div>
  </section>

  <section class="card card--back" aria-label="Card back">
    <h2 class="card-title">
      <span>The Bold</span>
      <span>Learner</span>
    </h2>
    <p class="tagline">Practical ways<br>to help learners<br>grow and thrive<br>in class<br>and beyond</p>
  </section>

</body>
</html>
```